Electrical Safety Inspection for High End Customers

Flyer designed to advertise a 50 point electrical safety check service available from a recent start up electrician's firm in Auckland, New Zealand. I am a registered electrical inspector with 16 years experience.
Targeting high end customers, so I want the flyer to have a premium feel to it (glossy black background, etc). The final design should communicate peace of mind. The price will be $60 incl. GST
The checks included should be 1) Mains Cable 2)Mains entry point 3)Switchboard 4)Circuit protection correctly rated 5)Circuit protection operational 6)The main earthing system 7)Safety systems 8)Light fittings 9)Socket outlets 10)Deterioration of fittings 11)Deterioration of cabling 12)Compliance with current regulations
I have included a copy of the test sheet for reference. I have also included my logo and the senior circuitry federation of New Zealand, both of which must be present.
Target Market(s)
High end home owners
Industry/Entity Type
Electrician
Colors
Designer to choose colors to be used in the design.
Look and feel

```html
<!DOCTYPE html>
<html lang="en">
<head>
<meta charset="utf-8">
<title>Volt Haven Electrical – Electrical Safety Inspection</title>
<link rel="stylesheet" href="https://fonts.googleapis.com/css2?family=Montserrat:wght@500;600;700;800;900&display=swap">
<style>
  :root {
    --page-bg: #d4d4d4;
    --paper-light: #eceeee;
    --ink: #0d0d0d;
    --black: #0b0b0b;
    --red: #ff0a0f;
    --blue-dark: #0a4fb8;
    --blue-light: #0a8ee8;
    --yellow: #ffd400;
    --white: #ffffff;
    --badge-blue: #1a4f8c;
  }
  * { box-sizing: border-box; margin: 0; padding: 0; }
  html, body { width: 1200px; height: 1200px; overflow: hidden; }
  body {
    background: var(--page-bg);
    font-family: "Montserrat", sans-serif;
    position: relative;
  }
  .flyer {
    position: absolute;
    left: 190px; top: 22px;
    width: 820px; height: 1156px;
    overflow: hidden;
    background: var(--paper-light);
  }
  .flyer-shapes { position: absolute; inset: 0; }
  .brand {
    position: absolute; left: 54px; top: 84px;
    display: flex; align-items: center; gap: 12px;
  }
  .brand-mark { width: 40px; height: 40px; background: var(--ink); border-radius: 50%; }
  .brand-name {
    font-weight: 800; font-size: 27px; color: var(--ink);
    letter-spacing: 0.5px; line-height: 1;
  }
  .headline {
    position: absolute; left: 50px; top: 180px; width: 320px;
    font-weight: 900; color: var(--ink); line-height: 1;
  }
  .headline span { display: block; }
  .headline .line-sm { font-size: 50px; letter-spacing: -0.5px; }
  .headline .line-lg { font-size: 72px; color: var(--red); letter-spacing: -1.5px; margin: 6px 0 4px; }
  .price-label {
    position: absolute; left: 54px; top: 407px;
    width: 124px; height: 38px;
    background: var(--red); color: var(--white);
    font-weight: 800; font-size: 24px; line-height: 38px; padding-left: 14px;
    clip-path: polygon(0 0, 78% 0, 100% 100%, 0 100%);
  }
  .price-value {
    position: absolute; left: 54px; top: 444px;
    width: 318px; height: 55px;
    background: linear-gradient(90deg, var(--blue-dark), var(--blue-light));
    color: var(--white); font-weight: 800; font-size: 42px;
    line-height: 55px; padding-left: 20px; letter-spacing: -0.5px;
  }
  .experience {
    position: absolute; left: 161px; top: 609px; width: 498px; height: 58px;
  }
  .experience svg { position: absolute; inset: 0; }
  .experience-text {
    position: absolute; inset: 0; text-align: center;
    color: var(--white); font-weight: 800; font-size: 36px; line-height: 58px;
  }
  .intro {
    position: absolute; left: 120px; top: 698px; width: 580px;
    text-align: center; color: var(--white);
    font-weight: 500; font-size: 19px; line-height: 25px;
  }
  .intro .hl-yellow { color: var(--yellow); font-weight: 700; }
  .intro .hl-red { color: var(--red); font-weight: 700; }
  .checklist {
    position: absolute; top: 801px; list-style: none;
    color: var(--white); font-weight: 500; font-size: 16px;
  }
  .checklist.col-left { left: 69px; }
  .checklist.col-right { left: 434px; }
  .checklist li { height: 29px; display: flex; align-items: center; gap: 13px; }
  .checklist svg { width: 15px; height: 15px; flex: none; }
  .member-badge {
    position: absolute; left: 70px; top: 1082px; width: 146px; height: 63px;
    background: var(--badge-blue);
  }
  .phone {
    position: absolute; left: 446px; top: 1043px; width: 303px; height: 51px;
    border: 2px solid var(--white); border-radius: 26px;
    display: flex; align-items: center; justify-content: center; gap: 10px;
    color: var(--white); font-weight: 800; font-size: 33px;
  }
  .phone svg { width: 26px; height: 26px; }
  .website {
    position: absolute; left: 446px; top: 1107px; width: 303px;
    display: flex; align-items: center; justify-content: center; gap: 6px;
    color: var(--white); font-weight: 500; font-size: 18px;
  }
  .website b { font-weight: 700; }
  .website svg { width: 18px; height: 18px; }
</style>
</head>
<body>
  <main class="flyer">
    <svg class="flyer-shapes" viewBox="0 0 820 1156" aria-hidden="false">
      <defs>
        <linearGradient id="photoTone" x1="0" y1="0" x2="1" y2="0">
          <stop offset="0" stop-color="#eceeee" stop-opacity="0"/>
          <stop offset="0.18" stop-color="#d8d9d6"/>
          <stop offset="0.55" stop-color="#a7a49b"/>
          <stop offset="1" stop-color="#8a8a82"/>
        </linearGradient>
        <linearGradient id="darkPanel" x1="0" y1="0" x2="1" y2="1">
          <stop offset="0" stop-color="#141414"/>
          <stop offset="0.5" stop-color="#0a0a0a"/>
          <stop offset="1" stop-color="#161616"/>
        </linearGradient>
      </defs>
      <rect x="300" y="0" width="520" height="560" fill="url(#photoTone)" role="img" aria-label="Photo of a smiling electrician in hard hat, safety glasses and hi-vis vest working on a switchboard"/>
      <polygon points="0,597 820,498 820,1156 0,1156" fill="url(#darkPanel)"/>
      <polygon points="0,1076 820,978 820,1156 0,1156" fill="#ff0a0f"/>
    </svg>

    <div class="brand">
      <span class="brand-mark"></span>
      <span class="brand-name">VOLT HAVEN ELECTRICAL</span>
    </div>

    <h1 class="headline">
      <span class="line-sm">ELECTRICAL</span>
      <span class="line-lg">SAFETY</span>
      <span class="line-sm">INSPECTION</span>
    </h1>

    <div class="price-label">PRICE</div>
    <div class="price-value">$60 incl. GST</div>

    <div class="experience">
      <svg viewBox="0 0 498 58" preserveAspectRatio="none" aria-hidden="true">
        <defs>
          <linearGradient id="ribbonBlue" x1="0" y1="0" x2="1" y2="0">
            <stop offset="0" stop-color="#0a4fb8"/>
            <stop offset="1" stop-color="#0a8ee8"/>
          </linearGradient>
        </defs>
        <polygon points="0,0 18,0 0,58" fill="#ff0a0f"/>
        <polygon points="498,58 480,58 498,0" fill="#ff0a0f"/>
        <polygon points="18,0 498,0 480,58 0,58" fill="url(#ribbonBlue)"/>
      </svg>
      <div class="experience-text">16 YEARS EXPERIENCE</div>
    </div>

    <p class="intro">
      <span class="hl-yellow">50 point electrical safety</span> check service available<br>
      from a recent start up electrician's firm<br>
      in <span class="hl-red">Auckland, New Zealand.</span>
    </p>

    <ul class="checklist col-left">
      <li><svg viewBox="0 0 16 16"><circle cx="8" cy="8" r="8" fill="#ff0a0f"/><path d="M4.5 8.3l2.3 2.3 4.7-4.8" stroke="#fff" stroke-width="2" fill="none"/></svg>Mains Cable</li>
      <li><svg viewBox="0 0 16 16"><circle cx="8" cy="8" r="8" fill="#ff0a0f"/><path d="M4.5 8.3l2.3 2.3 4.7-4.8" stroke="#fff" stroke-width="2" fill="none"/></svg>Mains entry point</li>
      <li><svg viewBox="0 0 16 16"><circle cx="8" cy="8" r="8" fill="#ff0a0f"/><path d="M4.5 8.3l2.3 2.3 4.7-4.8" stroke="#fff" stroke-width="2" fill="none"/></svg>Switchboard</li>
      <li><svg viewBox="0 0 16 16"><circle cx="8" cy="8" r="8" fill="#ff0a0f"/><path d="M4.5 8.3l2.3 2.3 4.7-4.8" stroke="#fff" stroke-width="2" fill="none"/></svg>Circuit protection correctly rated</li>
      <li><svg viewBox="0 0 16 16"><circle cx="8" cy="8" r="8" fill="#ff0a0f"/><path d="M4.5 8.3l2.3 2.3 4.7-4.8" stroke="#fff" stroke-width="2" fill="none"/></svg>Circuit protection operational</li>
      <li><svg viewBox="0 0 16 16"><circle cx="8" cy="8" r="8" fill="#ff0a0f"/><path d="M4.5 8.3l2.3 2.3 4.7-4.8" stroke="#fff" stroke-width="2" fill="none"/></svg>The main earthing system</li>
    </ul>
    <ul class="checklist col-right">
      <li><svg viewBox="0 0 16 16"><circle cx="8" cy="8" r="8" fill="#ff0a0f"/><path d="M4.5 8.3l2.3 2.3 4.7-4.8" stroke="#fff" stroke-width="2" fill="none"/></svg>Safety systems</li>
      <li><svg viewBox="0 0 16 16"><circle cx="8" cy="8" r="8" fill="#ff0a0f"/><path d="M4.5 8.3l2.3 2.3 4.7-4.8" stroke="#fff" stroke-width="2" fill="none"/></svg>Light fittings</li>
      <li><svg viewBox="0 0 16 16"><circle cx="8" cy="8" r="8" fill="#ff0a0f"/><path d="M4.5 8.3l2.3 2.3 4.7-4.8" stroke="#fff" stroke-width="2" fill="none"/></svg>Socket outlets</li>
      <li><svg viewBox="0 0 16 16"><circle cx="8" cy="8" r="8" fill="#ff0a0f"/><path d="M4.5 8.3l2.3 2.3 4.7-4.8" stroke="#fff" stroke-width="2" fill="none"/></svg>Deterioration of fittings</li>
      <li><svg viewBox="0 0 16 16"><circle cx="8" cy="8" r="8" fill="#ff0a0f"/><path d="M4.5 8.3l2.3 2.3 4.7-4.8" stroke="#fff" stroke-width="2" fill="none"/></svg>Deterioration of cabling</li>
      <li><svg viewBox="0 0 16 16"><circle cx="8" cy="8" r="8" fill="#ff0a0f"/><path d="M4.5 8.3l2.3 2.3 4.7-4.8" stroke="#fff" stroke-width="2" fill="none"/></svg>Compliance with current regulations</li>
    </ul>

    <div class="member-badge" role="img" aria-label="Member badge of the senior circuitry federation of New Zealand"></div>

    <div class="phone">
      <svg viewBox="0 0 24 24" aria-hidden="true"><path d="M6.6 10.8c1.4 2.8 3.8 5.1 6.6 6.6l2.2-2.2c.3-.3.7-.4 1-.2 1.1.4 2.3.6 3.6.6.6 0 1 .4 1 1V20c0 .6-.4 1-1 1C10.6 21 3 13.4 3 4c0-.6.4-1 1-1h3.5c.6 0 1 .4 1 1 0 1.3.2 2.5.6 3.6.1.3 0 .7-.2 1l-2.3 2.2z" fill="#fff"/></svg>
      <span>021 555 0143</span>
    </div>
    <div class="website">
      <svg viewBox="0 0 24 24" aria-hidden="true"><g fill="none" stroke="#fff" stroke-width="1.8"><circle cx="12" cy="12" r="9.5"/><ellipse cx="12" cy="12" rx="4" ry="9.5"/><path d="M2.5 12h19M4 7h16M4 17h16"/></g></svg>
      <span>www.<b>volthavenelectrical</b>.co.nz</span>
    </div>
  </main>
</body>
</html>
```